Flyer for Roadhaven 41Ter - Fresh Food Vending Machine in Helchteren

Project Description:
Roadhaven 41Ter has placed a new fresh food vending machine in Helchteren at KP Sodas (Lindeweg 517). We want to create an eye-catching, modern flyer to inform local residents about this vending machine and invite them to visit. The flyer will be distributed door-to-door in Helchteren.
Target Audience:
Residents of Helchteren and surrounding areas.
People looking for quick, fresh meals such as daily specials, wraps, poke bowls, soups, and pasta dishes.
Key Message:
Main title: "Helchteren, we’re here!"
Location: "Our brand-new fresh food vending machine is now at KP Sodas, Lindeweg 517!"
Available products: "Daily specials, wraps, poke bowls, soups, pasta dishes, and more."
Promotion: "For a limited time: with every product, you’ll receive a scratch card, and you always win!"
Style Guidelines:
Clean, professional, and inviting design.
Follow the new branding style of Roadhaven 41Ter (refer to the most recent posts on our Instagram and Facebook pages). Or see attachment for the layout inspiration.
Instagram: www.pictagram-example.com/roadhaven41ter
Facebook: www.friendbook-example.com/Roadhaven41
Do not use the older branding visible in earlier posts.
Format:
Flyer size: A5 (148 x 210 mm).
Additional Information:
Include our logos and social media accounts on the flyer.
Add a clear call-to-action, such as: "Visit us today!"
Ensure the flyer is easy to read and that all information is clear at a glance.
We look forward to seeing your creative and inspiring designs!

```html
<!DOCTYPE html>
<html lang="en">
<head>
<meta charset="utf-8">
<title>Roadhaven 41Ter – Helchteren, we're here!</title>
<link href="https://fonts.googleapis.com/css2?family=Bebas+Neue&family=Pacifico&family=Roboto:ital,wght@0,300;0,400;1,500;1,700&display=swap" rel="stylesheet">
<style>
  :root{
    --navy:#2a2a5c;
    --sky:#00aaff;
    --blue:#0a7fcc;
    --paper:#eeeeee;
    --yellow:#ffee00;
    --red:#e8141b;
    --ink:#111;
    --grey:#555;
  }
  *{margin:0;padding:0;box-sizing:border-box}
  html,body{width:848px;height:1200px;overflow:hidden;background:var(--paper)}
  .flyer{position:relative;width:848px;height:1200px;overflow:hidden;background:var(--paper);font-family:'Roboto',sans-serif}
  .side-shape,.bottom-shape{position:absolute;left:0;top:0}
  .hero-photo{position:absolute;left:0;top:0;width:688px;height:925px;
    background:linear-gradient(160deg,#d8d6d0 0%,#3a3d44 22%,#1d2128 50%,#2c3340 75%,#151820 100%)}
  .hero-band{position:absolute;left:0;top:704px;width:688px;height:221px;background:rgba(18,20,48,.88)}
  .headline{position:absolute;left:44px;top:716px;font-family:'Bebas Neue',sans-serif;font-size:152px;line-height:1;color:var(--sky);letter-spacing:-1px}
  .headline-script{position:absolute;left:304px;top:812px;font-family:'Pacifico',cursive;font-size:58px;line-height:1.2;color:#fff}
  .socials{position:absolute;left:748px;top:159px;display:flex;flex-direction:column;gap:10px}
  .socials span{display:block;width:22px;height:22px;border-radius:50%;background:var(--navy)}
  .website{position:absolute;left:762px;top:637px;transform:translate(-50%,-50%) rotate(-90deg);white-space:nowrap;color:#fff;font-size:17px;letter-spacing:1.5px}
  .specials{position:absolute;left:56px;top:978px}
  .specials h2{font-style:italic;font-weight:700;font-size:21px;color:var(--red)}
  .specials p{margin-top:8px;font-weight:300;font-size:18px;color:var(--grey)}
  .brand{position:absolute;left:58px;top:1100px;display:flex;align-items:center;gap:8px;font-weight:400;font-size:22px;color:var(--navy)}
  .brand i{display:block;width:16px;height:16px;background:var(--blue)}
  .location{position:absolute;left:257px;top:1086px;font-style:italic;font-weight:500;font-size:16.5px;line-height:1.3;color:var(--navy)}
  .location em{color:var(--blue)}
  .dot{position:absolute;border-radius:50%;background:var(--blue)}
  .dot-grid{position:absolute;left:539px;top:1062px;display:grid;grid-template-columns:6px 6px;gap:8.5px 9px}
  .dot-grid span{width:6px;height:6px;border-radius:50%;background:var(--navy)}
  .offer{position:absolute;left:638px;top:895px;width:181px;height:244px}
  .offer svg{position:absolute;inset:0}
  .offer-body{position:relative;text-align:center;color:var(--navy)}
  .offer-title{padding-top:10px;font-family:'Bebas Neue',sans-serif;font-size:44px;line-height:.86}
  .offer-rule{margin:10px 4px 0;border-top:5px dotted var(--navy)}
  .offer-text{margin-top:16px;font-size:15.5px;line-height:1.3}
  .offer-card{margin:4px 4px 0;background:var(--ink);color:#fff;font-family:'Pacifico',cursive;font-size:19px;line-height:32px}
  .offer-win{margin-top:7px;font-size:16px}
</style>
</head>
<body>
<div class="flyer">
  <svg class="side-shape" width="848" height="1200" aria-hidden="true">
    <path d="M693 410 L848 343 L848 1200 L693 1200 Z" fill="var(--navy)"/>
  </svg>

  <div class="hero-photo" role="img" aria-label="Photo of fresh food vending machines stocked with snacks and packaged meals"></div>
  <div class="hero-band"></div>

  <svg class="bottom-shape" width="848" height="1200" aria-hidden="true">
    <path d="M517 925 C570 955 585 1020 582 1080 C580 1140 588 1180 592 1200 L848 1200 L848 925 Z" fill="var(--navy)"/>
  </svg>

  <h1 class="headline">HELCHTEREN,</h1>
  <p class="headline-script">we're here!</p>

  <div class="socials" aria-label="Social media"><span></span><span></span><span></span><span></span></div>
  <p class="website">www.roadhaven41ter-example.com</p>

  <section class="specials">
    <h2>DAILY SPECIALS:</h2>
    <p>Wraps, Poke Bowls, Soups, Pasta Dishes, &amp; more.</p>
  </section>

  <div class="brand"><i></i>Roadhaven 41Ter</div>
  <p class="location">Our brand-new fresh food<br>vending machine is now at<br><em>KP Sodas, Lindeweg 517!</em></p>

  <span class="dot" style="left:480px;top:1041px;width:32px;height:32px"></span>
  <div class="dot-grid"><span></span><span></span><span></span><span></span><span></span><span></span><span></span><span></span></div>
  <span class="dot" style="left:620px;top:1107px;width:116px;height:116px"></span>
  <span class="dot" style="left:484px;top:1183px;width:28px;height:28px"></span>

  <div class="offer">
    <svg width="181" height="244" aria-hidden="true">
      <path d="M14 0 H167 A14 14 0 0 0 181 14 V230 A14 14 0 0 0 167 244 H14 A14 14 0 0 0 0 230 V14 A14 14 0 0 0 14 0 Z" fill="var(--yellow)"/>
    </svg>
    <div class="offer-body">
      <p class="offer-title">LIMITED<br>TIME OFFER</p>
      <div class="offer-rule"></div>
      <p class="offer-text">With Every Product,<br>You'll Receive a</p>
      <p class="offer-card">Scratch Card,</p>
      <p class="offer-win">&amp; You Always Win!</p>
    </div>
  </div>
</div>
</body>
</html>
```